American cannabis tech company business card design

Thrum.com is seeking a modern, professional, and brand-aligned business card that represents our company and its core values: Mission, Story, Values, and Impact. As an innovative cannabis company, we want a business card that is not only visually appealing but also serves as a representation of who we are and what we stand for.

Project Scope: Design a double-sided business card that integrates our brand identity and core values. Incorporate our key brand elements, ensuring a sleek and contemporary aesthetic. Visually reflect our core values (Mission, Story, Values, Impact) in a way that is engaging yet professional.

Target Market(s)

Vendors, third parties,

Contact Information for Business Card

Contact details (name, title, email, phone, website, etc.)

Font styles to use
Other font styles liked:
• Caslon, Centra

Colors

Designer to choose colors to be used in the design.

Requirements
Must have
• Thrum.com logo and branding A creative yet clean way to integrate our core values (Mission, Story, Values, Impact) Modern typography and a well-structured layout
Nice to have
• forest green, grey, white, black
Should not have
• references to marijuana, leafs, plants, or related product

```html
<!DOCTYPE html>
<html lang="en">
<head>
<meta charset="utf-8">
<title>Thrum – Business Card</title>
<link href="https://fonts.googleapis.com/css2?family=Figtree:wght@400;500;700;800&display=swap" rel="stylesheet">
<style>
  :root {
    --backdrop: #999999;
    --card-white: #ffffff;
    --forest: #1b3220;
    --forest-deep: #19301d;
    --forest-light: #22432a;
    --rule: #6f6f62;
    --ink-light: #ffffff;
  }
  * { margin: 0; padding: 0; box-sizing: border-box; }
  html, body {
    width: 1200px; height: 1000px; overflow: hidden;
    background: var(--backdrop);
    font-family: "Figtree", "Helvetica Neue", Arial, sans-serif;
    color: var(--forest);
  }
  .canvas { position: relative; width: 1200px; height: 1000px; }
  .card {
    position: absolute; left: 253px; width: 694px; height: 400px;
    border-radius: 24px; overflow: hidden;
  }
  .card-front { top: 107px; background: var(--card-white); }
  .card-back { top: 545px; background: var(--forest); }

  .wordmark {
    position: absolute; left: 48px; top: 76px;
    font-size: 52px; font-weight: 800; letter-spacing: 0.5px;
    line-height: 1; color: var(--forest);
  }
  .person-name {
    position: absolute; left: 48px; top: 238px;
    font-size: 29px; font-weight: 700; line-height: 1;
  }
  .person-title {
    position: absolute; left: 50px; top: 270px;
    font-size: 19px; font-weight: 400; line-height: 1;
  }
  .divider {
    position: absolute; left: 50px; top: 302px; width: 586px;
    height: 2px; background: var(--rule);
  }
  .contact {
    position: absolute; left: 50px; top: 313px;
    font-size: 17px; line-height: 22px;
  }
  .website {
    position: absolute; right: 56px; top: 340px;
    font-size: 17px; line-height: 22px;
  }
  .website strong { font-weight: 700; }

  .pattern-field {
    position: absolute; inset: 0;
    background: linear-gradient(90deg, var(--forest-deep) 0%, var(--forest) 45%, var(--forest-light) 100%);
  }
  .core-values {
    position: absolute; right: 98px; top: 292px;
    font-size: 23px; font-weight: 700; color: var(--ink-light); line-height: 1;
    white-space: nowrap;
  }
</style>
</head>
<body>
<main class="canvas">
  <section class="card card-front" aria-label="Business card front">
    <div class="wordmark">THRUM</div>
    <div class="person-name">Daniel Carver</div>
    <div class="person-title">Co-Founder &amp; CEO</div>
    <div class="divider"></div>
    <div class="contact">405-555-0148<br>name@thrum.com</div>
    <div class="website"><strong>thrum</strong>.com</div>
  </section>

  <section class="card card-back" aria-label="Business card back">
    <div class="pattern-field" role="img" aria-label="Repeating tone-on-tone brand monogram pattern in forest greens"></div>
    <div class="core-values">Mission. Story. Values. Impact.</div>
  </section>
</main>
</body>
</html>
```